American cannabis tech company business card design

Thrum.com is seeking a modern, professional, and brand-aligned business card that represents our company and its core values: Mission, Story, Values, and Impact. As an innovative cannabis company, we want a business card that is not only visually appealing but also serves as a representation of who we are and what we stand for.

Project Scope: Design a double-sided business card that integrates our brand identity and core values. Incorporate our key brand elements, ensuring a sleek and contemporary aesthetic. Visually reflect our core values (Mission, Story, Values, Impact) in a way that is engaging yet professional.

Target Market(s)

Vendors, third parties,

Contact Information for Business Card

Contact details (name, title, email, phone, website, etc.)

Font styles to use
Other font styles liked:
• Caslon, Centra

Colors

Designer to choose colors to be used in the design.

Requirements
Must have
• Thrum.com logo and branding A creative yet clean way to integrate our core values (Mission, Story, Values, Impact) Modern typography and a well-structured layout
Nice to have
• forest green, grey, white, black
Should not have
• references to marijuana, leafs, plants, or related product

```html
<!DOCTYPE html>
<html lang="en">
<head>
<meta charset="utf-8">
<title>Thrum.com Business Card</title>
<link rel="stylesheet" href="https://fonts.googleapis.com/css2?family=Jost:wght@400;500;600;800&display=swap">
<style>
  :root {
    --stage: #1b1b1b;
    --card-dark: #2a2527;
    --forest: #1d6b3a;
    --forest-deep: #0f4225;
    --wave: #23913f;
    --white: #ffffff;
    --muted: #cfd8d2;
    --rule: rgba(255,255,255,0.55);
  }
  * { box-sizing: border-box; margin: 0; padding: 0; }
  html, body { width: 1200px; height: 900px; overflow: hidden; }
  body {
    background: radial-gradient(ellipse at 60% 45%, #3a3a3a 0%, var(--stage) 70%);
    font-family: "Jost", sans-serif;
    color: var(--white);
    position: relative;
  }
  .card {
    position: absolute;
    width: 520px;
    height: 300px;
    background: var(--card-dark);
    overflow: hidden;
    box-shadow: 0 18px 40px rgba(0,0,0,0.55);
  }
  .card::before {
    content: "";
    position: absolute; inset: 0;
    background: linear-gradient(150deg, var(--forest) 0%, var(--forest-deep) 38%, rgba(15,66,37,0) 66%);
  }
  .card--front { left: 60px; top: 440px; }
  .card--back { left: 620px; top: 160px; }

  .wave-band { position: absolute; left: 0; top: 0; width: 520px; height: 300px; }

  .star-grid {
    position: absolute;
    width: 40px; height: 18px;
    background: rgba(255,255,255,0.35);
    border-radius: 2px;
  }

  .wordmark {
    position: absolute;
    font-weight: 800;
    font-size: 58px;
    letter-spacing: 1px;
    color: var(--white);
    line-height: 1;
  }
  .card--front .wordmark { right: 40px; top: 118px; }
  .card--back .wordmark { left: 50%; top: 50%; transform: translate(-50%, -50%); }

  .contact-block { position: absolute; left: 34px; top: 44px; width: 250px; }
  .contact-block .rule { height: 1px; background: var(--rule); width: 210px; }
  .person-name { font-weight: 600; font-size: 26px; margin-top: 10px; line-height: 1.1; }
  .person-title { font-size: 13px; color: var(--muted); margin-top: 2px; margin-bottom: 10px; }
  .contact-list { list-style: none; margin-top: 12px; }
  .contact-list li {
    display: flex; align-items: center; gap: 9px;
    font-size: 11.5px; margin-bottom: 7px; color: var(--white);
  }
  .contact-icon {
    width: 16px; height: 16px; border-radius: 4px;
    background: var(--white);
    display: flex; align-items: center; justify-content: center;
    flex: none;
  }
  .contact-icon svg { width: 11px; height: 11px; }
</style>
</head>
<body>

  <section class="card card--back" aria-label="Card back">
    <svg class="wave-band" viewBox="0 0 520 300" role="img" aria-label="Flowing green striped wave decoration">
      <defs>
        <linearGradient id="waveBack" x1="0" y1="0" x2="1" y2="1">
          <stop offset="0" stop-color="#1f7a3b"/>
          <stop offset="1" stop-color="#23913f"/>
        </linearGradient>
      </defs>
      <path d="M150 0 L520 0 L520 110 C460 100 400 70 330 52 C260 34 200 30 150 0 Z" fill="url(#waveBack)" opacity="0.85"/>
      <path d="M0 225 C90 215 160 240 250 262 C340 284 430 280 520 272 L520 300 L0 300 Z" fill="url(#waveBack)"/>
    </svg>
    <div class="star-grid" style="left:18px; top:16px;"></div>
    <div class="star-grid" style="right:22px; bottom:130px;"></div>
    <div class="wordmark">THRUM</div>
  </section>

  <section class="card card--front" aria-label="Card front">
    <svg class="wave-band" viewBox="0 0 520 300" role="img" aria-label="Flowing green striped wave decoration">
      <defs>
        <linearGradient id="waveFront" x1="0" y1="0" x2="1" y2="1">
          <stop offset="0" stop-color="#1f7a3b"/>
          <stop offset="1" stop-color="#23913f"/>
        </linearGradient>
      </defs>
      <path d="M0 205 C80 195 150 215 230 240 C310 265 420 282 520 276 L520 300 L0 300 Z" fill="url(#waveFront)"/>
    </svg>
    <div class="star-grid" style="left:150px; top:14px;"></div>
    <div class="star-grid" style="left:14px; top:14px;"></div>
    <div class="star-grid" style="right:60px; top:196px;"></div>

    <div class="contact-block">
      <div class="rule"></div>
      <h1 class="person-name">Dana Whitfield</h1>
      <p class="person-title">Senior Manager</p>
      <div class="rule"></div>
      <ul class="contact-list">
        <li>
          <span class="contact-icon"><svg viewBox="0 0 12 12"><path d="M3 1.5 L4.6 3.4 L3.8 4.6 C4.4 6 5.9 7.5 7.4 8.2 L8.6 7.4 L10.5 9 L9.4 10.5 C6 10.2 1.8 6 1.5 2.6 Z" fill="#1d6b3a"/></svg></span>
          +1 555-010-4821
        </li>
        <li>
          <span class="contact-icon"><svg viewBox="0 0 12 12"><rect x="1" y="2.5" width="10" height="7" rx="1" fill="none" stroke="#1d6b3a" stroke-width="1.3"/><path d="M1.5 3 L6 6.6 L10.5 3" fill="none" stroke="#1d6b3a" stroke-width="1.3"/></svg></span>
          hello@thrumteam.com
        </li>
        <li>
          <span class="contact-icon"><svg viewBox="0 0 12 12"><path d="M6 11 C3 7.5 2.5 6 2.5 4.5 A3.5 3.5 0 0 1 9.5 4.5 C9.5 6 9 7.5 6 11 Z" fill="#1d6b3a"/><circle cx="6" cy="4.5" r="1.3" fill="#fff"/></svg></span>
          Pine Hollow, VT • Cedar Falls, WV.
        </li>
        <li>
          <span class="contact-icon"><svg viewBox="0 0 12 12"><circle cx="6" cy="6" r="4.5" fill="none" stroke="#1d6b3a" stroke-width="1.2"/><ellipse cx="6" cy="6" rx="2" ry="4.5" fill="none" stroke="#1d6b3a" stroke-width="1"/><path d="M1.5 6 H10.5" stroke="#1d6b3a" stroke-width="1"/></svg></span>
          www.thrum.com
        </li>
      </ul>
    </div>

    <div class="wordmark">THRUM</div>
  </section>

</body>
</html>
```